Business Card Design Project

Business card based on attached logo

Tod Mulvey
Tod@lorvanquiz.com
888-517-4069 ext. 615
Www.LorvanQuiz.com

Industry/Entity Type

Business

```html
<!DOCTYPE html>
<html lang="en">
<head>
<meta charset="utf-8">
<title>LorvanQuiz Business Card</title>
<link href="https://fonts.googleapis.com/css2?family=Roboto+Condensed:wght@400;600;700&display=swap" rel="stylesheet">
<style>
  :root {
    --canvas: #e6e6e8;
    --card-white: #ffffff;
    --card-black: #050505;
    --ink: #1f1f1f;
    --accent: #e8262c;
    --paper-light: #ffffff;
  }
  html, body {
    margin: 0;
    padding: 0;
    width: 1200px;
    height: 960px;
    overflow: hidden;
    background: var(--canvas);
    font-family: "Roboto Condensed", Arial, sans-serif;
  }
  .stage {
    position: relative;
    width: 1200px;
    height: 960px;
  }
  .card {
    position: absolute;
    top: 325px;
    width: 540px;
    height: 309px;
    box-sizing: border-box;
    box-shadow: 0 8px 24px rgba(0,0,0,0.18);
  }
  .card--front {
    left: 40px;
    background: var(--card-white);
  }
  .card--back {
    left: 620px;
    background: var(--card-black);
  }
  .brand {
    position: absolute;
    display: flex;
    align-items: center;
    gap: 10px;
    font-weight: 700;
    letter-spacing: -0.5px;
    line-height: 1;
  }
  .brand__mark {
    width: 14px;
    height: 14px;
    background: var(--accent);
  }
  .card--front .brand {
    left: 56px;
    top: 70px;
    font-size: 64px;
    color: var(--ink);
  }
  .card--back .brand {
    left: 50%;
    top: 50%;
    transform: translate(-50%, -50%);
    font-size: 58px;
    color: var(--paper-light);
  }
  .person {
    position: absolute;
    right: 34px;
    top: 172px;
    text-align: right;
    color: var(--ink);
  }
  .person__name {
    font-size: 22px;
    font-weight: 600;
    line-height: 1.05;
  }
  .person__role {
    font-size: 13px;
    font-weight: 600;
  }
  .contact {
    position: absolute;
    right: 34px;
    bottom: 26px;
    margin: 0;
    padding: 0;
    list-style: none;
    color: var(--ink);
    font-size: 14px;
    line-height: 19px;
    text-align: right;
  }
  .contact__item {
    display: flex;
    justify-content: flex-end;
    align-items: center;
    gap: 6px;
  }
  .contact__icon {
    width: 10px;
    height: 10px;
    fill: var(--accent);
    flex: none;
  }
</style>
</head>
<body>
<main class="stage">
  <section class="card card--front" aria-label="Business card front">
    <div class="brand"><span class="brand__name">LorvanQuiz</span><span class="brand__mark"></span></div>
    <div class="person">
      <div class="person__name">Tod Mulvey</div>
      <div class="person__role">Owner</div>
    </div>
    <ul class="contact">
      <li class="contact__item">P O Box 5820, Kestrel Hill AU
        <svg class="contact__icon" viewBox="0 0 10 10"><path d="M5 0.5 L10 5 H8.5 V9.5 H6 V6.5 H4 V9.5 H1.5 V5 H0 Z"/></svg>
      </li>
      <li class="contact__item">888-517-4069 ext. 615
        <svg class="contact__icon" viewBox="0 0 10 10"><path d="M2 0.5 L3.8 0.5 L4.3 3 L3 4 Q4 6.2 6 7 L7 5.7 L9.5 6.2 L9.5 8 Q9.5 9.5 8 9.5 Q0.5 9 0.5 2 Q0.5 0.5 2 0.5 Z"/></svg>
      </li>
      <li class="contact__item">Tod@lorvanquiz.com
        <svg class="contact__icon" viewBox="0 0 10 10"><path d="M0 2 H10 V8.5 H0 Z" /><path d="M0 2 L5 5.5 L10 2" fill="none" stroke="#fff" stroke-width="0.9"/></svg>
      </li>
      <li class="contact__item">www.lorvanquiz.com
        <svg class="contact__icon" viewBox="0 0 10 10"><circle cx="5" cy="5" r="4.6"/><path d="M0.5 5 H9.5 M5 0.5 V9.5 M5 0.5 Q2 5 5 9.5 M5 0.5 Q8 5 5 9.5" fill="none" stroke="#fff" stroke-width="0.7"/></svg>
      </li>
    </ul>
  </section>

  <section class="card card--back" aria-label="Business card back">
    <div class="brand"><span class="brand__name">LorvanQuiz</span><span class="brand__mark"></span></div>
  </section>
</main>
</body>
</html>
```